KA VERLINE

We need a letterhead design for an Image & Etiquette Consultancy company based in Singapore.

The services we provide are Personal Image Consultation, Image & Etiquette Workshop for schools and corporate.

The design should have our corporate colour as seen in the logo files I have uploaded.

Since our company helps clients with their image, the design should be aesthetically very appealing. It should reflect a very classy & elegant feel.

I will print the letterhead using my printer but most of the time will use it to write letters to my clients therefore the format should include MS Word.

```html
<!DOCTYPE html>
<html lang="en">
<head>
<meta charset="utf-8">
<title>KA VERLINE Letterhead</title>
<link href="https://fonts.googleapis.com/css2?family=Questrial&display=swap" rel="stylesheet">
<style>
  :root {
    --paper: #ffffff;
    --plum: #2f1446;
    --gold: #e9b517;
    --cream: #fbf3c8;
    --rule: #858585;
    --ink: #4a4a4a;
    --ghost: #e3e3e6;
  }
  * { margin: 0; padding: 0; box-sizing: border-box; }
  html, body { width: 971px; height: 1200px; overflow: hidden; background: var(--paper); }
  .letterhead {
    position: relative;
    width: 971px;
    height: 1200px;
    background: var(--paper);
    font-family: "Questrial", sans-serif;
    color: var(--ink);
  }
  .header-band { position: absolute; top: 34px; height: 88px; }
  .header-band--left { left: 0; width: 207px; background: linear-gradient(90deg, var(--gold) 0%, var(--cream) 100%); }
  .header-band--right { right: 0; width: 204px; background: linear-gradient(90deg, var(--cream) 0%, var(--gold) 100%); }
  .header-plate { position: absolute; left: 183px; top: 0; width: 607px; height: 160px; }
  .company-name {
    position: absolute; left: 207px; top: 48px; width: 560px;
    text-align: center;
    font-size: 60px; letter-spacing: 2px; line-height: 1;
    color: var(--gold);
  }
  .footer-name {
    position: absolute; left: 0; right: 0; top: 1022px;
    text-align: center; font-size: 52px; letter-spacing: 1px; line-height: 1; color: var(--ghost);
  }
  .footer-address {
    position: absolute; left: 0; right: 0; top: 1090px;
    text-align: center; font-size: 14px; color: var(--ink);
  }
  .footer-rule {
    position: absolute; left: 65px; width: 838px; top: 1122px;
    height: 4px; background: var(--rule);
  }
  .contact-row {
    position: absolute; left: 65px; width: 838px; top: 1142px;
    display: flex; justify-content: space-between; align-items: center;
    font-size: 15px; color: var(--ink);
  }
  .contact { display: flex; align-items: center; gap: 8px; }
  .contact--phone { font-size: 19px; }
  .contact svg { fill: var(--ink); }
</style>
</head>
<body>
<main class="letterhead">
  <div class="header-band header-band--left"></div>
  <div class="header-band header-band--right"></div>
  <svg class="header-plate" viewBox="0 0 607 160" aria-hidden="true">
    <polygon points="0,0 607,0 584,34 584,160 24,160 24,34" fill="var(--plum)"/>
  </svg>
  <div class="company-name">KA VERLINE</div>

  <div class="footer-name">KA VERLINE</div>
  <div class="footer-address">Suite000, Cityname, Countryname.</div>
  <div class="footer-rule"></div>
  <div class="contact-row">
    <span class="contact contact--phone">
      <svg width="12" height="20" viewBox="0 0 12 20"><rect x="1" y="3" width="10" height="16" rx="2"/><rect x="7" y="0" width="2" height="4"/><rect x="3" y="6" width="6" height="4" fill="#fff"/></svg>
      01234567890
    </span>
    <span class="contact">
      <svg width="16" height="12" viewBox="0 0 16 12"><rect x="0" y="2" width="16" height="10" rx="1"/><polyline points="1,3 8,8 15,3" fill="none" stroke="#fff" stroke-width="1.4"/></svg>
      Email: kaverline@poise.com
    </span>
    <span class="contact">
      <svg width="16" height="16" viewBox="0 0 16 16"><circle cx="8" cy="8" r="7" fill="none" stroke="var(--ink)" stroke-width="1.5"/><ellipse cx="8" cy="8" rx="3" ry="7" fill="none" stroke="var(--ink)" stroke-width="1.2"/><line x1="1" y1="8" x2="15" y2="8" stroke="var(--ink)" stroke-width="1.2"/></svg>
      kaverlinepoise.com
    </span>
  </div>
</main>
</body>
</html>
```